Silver Creek Plumbing Business card & letter head design

We need a new business card and letter head for our plumbing company called silver creek plumbing. attached is the companys logo. We provide domestic and commercial plumbing services in regional western Australia. We are after Something simple yet nice to look at and something that fits within the trade industry.

Target Market(s)

trade/building industry

Contact Information for Business Card

Darl Hensby
Manager
0461 238 574
enquiries@scplumbwork.net.au
ABN: 47 381 905 462
PCL: 5187

Domestic & Commercial Plumbing
Tip Truck & Excavator hire

Colors

Designer to choose colors to be used in the design.

```html
<!DOCTYPE html>
<html lang="en">
<head>
<meta charset="utf-8">
<title>Silver Creek Plumbing Letterhead</title>
<link href="https://fonts.googleapis.com/css2?family=Open+Sans:wght@400;600;700&display=swap" rel="stylesheet">
<style>
  :root {
    --backdrop: #e9e9ea;
    --paper: #ffffff;
    --brand-blue: #0b57a8;
    --band-grey: #555659;
    --ink: #222222;
    --muted: #444444;
    --band-text: #ffffff;
  }
  * { box-sizing: border-box; margin: 0; padding: 0; }
  html, body {
    width: 1200px; height: 944px; overflow: hidden;
    background: var(--backdrop);
    font-family: "Open Sans", Arial, sans-serif;
  }
  .letterhead {
    position: absolute; left: 280px; top: 20px;
    width: 640px; height: 904px;
    background: var(--paper);
    box-shadow: 0 6px 24px rgba(0,0,0,0.12);
    color: var(--ink);
  }
  .side-band {
    position: absolute; left: 0; top: 0; width: 32px; height: 100%;
    display: flex; flex-direction: column;
  }
  .side-band__registration {
    height: 218px; background: var(--band-grey);
    display: flex; align-items: center; justify-content: center;
  }
  .side-band__mark {
    height: 38px; background: var(--paper);
    display: flex; align-items: center; justify-content: center;
  }
  .side-band__mark span {
    width: 14px; height: 14px; border-radius: 50%; background: var(--brand-blue);
  }
  .side-band__contacts {
    flex: 1; background: var(--brand-blue);
    display: flex; align-items: center; justify-content: center;
  }
  .vertical-text {
    writing-mode: vertical-rl; transform: rotate(180deg);
    color: var(--band-text); font-size: 8.5px; letter-spacing: 0.2px;
    display: flex; align-items: center; gap: 34px; white-space: nowrap;
  }
  .contact-item { display: flex; align-items: center; gap: 6px; }
  .contact-item svg { width: 10px; height: 10px; fill: var(--band-text); transform: rotate(90deg); }
  .brand-name {
    position: absolute; left: 330px; top: 88px;
    font-size: 17px; font-weight: 700; color: var(--brand-blue);
    letter-spacing: 0.3px;
  }
  .letter {
    position: absolute; left: 112px; top: 328px; width: 480px;
    font-size: 10.5px; line-height: 17px; color: var(--ink);
  }
  .recipient { margin-bottom: 24px; }
  .salutation { margin-bottom: 14px; }
  .letter p { margin-bottom: 22px; }
  .signature {
    width: 120px; height: 34px; margin-top: 32px; margin-bottom: 4px;
    background: linear-gradient(90deg, #f1f1f1, #e4e4e4);
  }
  .signatory-name { font-weight: 700; font-size: 11px; }
  .signatory-role { color: var(--muted); }
</style>
</head>
<body>
  <main class="letterhead">
    <aside class="side-band">
      <div class="side-band__registration">
        <div class="vertical-text"><span>ABN: 47 381 905 462 &nbsp;|&nbsp; PCL: 5187</span></div>
      </div>
      <div class="side-band__mark"><span></span></div>
      <div class="side-band__contacts">
        <div class="vertical-text">
          <span class="contact-item"><svg viewBox="0 0 10 10"><path d="M5 0C3 3 2 4.5 2 6.2A3 3 0 0 0 8 6.2C8 4.5 7 3 5 0Z"/></svg>12 Quarry Road Geraldton, WA 6530</span>
          <span class="contact-item"><svg viewBox="0 0 10 10"><path d="M2 0h2l1 2.5-1.3 1a6 6 0 0 0 2.8 2.8l1-1.3L10 6v2c0 1-1 2-2 2A8 8 0 0 1 0 2c0-1 1-2 2-2Z"/></svg>0461 238 574</span>
          <span class="contact-item"><svg viewBox="0 0 10 10"><path d="M0 2h10v6H0Z M0 2l5 3.5L10 2" stroke="#0b57a8" stroke-width="0.8"/></svg>enquiries@scplumbwork.net.au</span>
          <span class="contact-item"><svg viewBox="0 0 10 10"><circle cx="5" cy="5" r="4.5"/></svg>scplumbwork.net.au</span>
        </div>
      </div>
    </aside>

    <div class="brand-name">Silver Creek Plumbing</div>

    <section class="letter">
      <div class="recipient">Mr/s<br>First &amp; Last name<br>Company Name<br>Address</div>
      <div class="salutation">Dear Sir</div>
      <p>This is a sample letter that has been placed to demonstrate typing remat (Your Company). letterhead design. When positioned properly, it will serve to work in harmony with all other elements letterhead. This letterhead design is meant to project an image</p>
      <p>This letterhead design is meant project an image of professionalism reliability. By using simple aligen we have created a very spacious feeling. The simplicity suggest rengththe spaciousnes contributes h aesthetics the layout. These basic qualities along with te (Your Company)</p>
      <p>look and helps reinforce the (Your Company) brand. letterhead design is meant to project an image p design. When positioned properly, it will serve to work in harmony all the other elements letterhead. sionalism and reliability.</p>
      <p>This letterhead design is based on the (Form of your logo) form (Your Company) logo. Each stationery we have created a very spacious feeling. The simplicity suggests strength the spaciousnes contribute part of the (Form of your logo).</p>
      <div class="signature" role="img" aria-label="Handwritten signature of Darl Hensby"></div>
      <div class="signatory-name">Darl Hensby</div>
      <div class="signatory-role">Manager</div>
    </section>
  </main>
</body>
</html>
```